Business Card and Letterhead for new company Vardel GreenWorks, Inc.

Vardel GreenWorks, Inc., an engineering and construction firm that provides services for solid waste landfill gas systems, needs a business card and letterhead. We recently had a logo designed but we are open to some tweaks to logo design and color scheme. Generally, we like "earthy" color tones - greens, browns, oranges. This is a sister company - www.talvoriengineering.example.

Target Market(s)

Solid waste landfill companies - Brindle Disposal, Halcott Hauling, etc.

Industry/Entity Type

Engineering and Construction

Contact Information for Business Card

Name, Title, email, mobile phone, work phone, website. Potential list of services for back of card: LFG Engineering and Design, GCCS Planning and Operational Consulting, Compliance Monitoring and Reporting, Routine Operations & Maintenance, Nonroutine O&M, Construction Management, Construction QA, GCCS Construction

Font styles to use
Sans Serif

Requirements
Must have
• Logo, pertinent information, maybe a tagline (still in development)
Nice to have
• For back of card, considering an engineering scale (attached for another business of ours), but want to look at other options, alternatives. Like the idea of the back of card to have some utility (scale, unit conversion info, list of services) but willing to consider lots of options.
Should not have
• Needs to have a professional (engineering) and technical look, not cartoonish.

```html
<!DOCTYPE html>
<html lang="en">
<head>
<meta charset="utf-8">
<title>Vardel GreenWorks – Business Card</title>
<link href="https://fonts.googleapis.com/css2?family=Montserrat:wght@400;500;700&family=Roboto+Condensed:wght@700&family=Arimo:wght@400&display=swap" rel="stylesheet">
<style>
  :root {
    --backdrop: #3b3b3b;
    --paper: #ffffff;
    --leaf-green: #77b32f;
    --earth-brown: #9a6634;
    --flame-orange: #f26a12;
    --ink: #1f1f1f;
  }
  * { box-sizing: border-box; margin: 0; padding: 0; }
  html, body { width: 1200px; height: 694px; overflow: hidden; }
  body {
    background: var(--backdrop);
    display: flex;
    align-items: center;
    justify-content: center;
    gap: 40px;
    font-family: "Montserrat", sans-serif;
  }
  .card {
    position: relative;
    width: 540px;
    height: 309px;
    background: var(--paper);
    overflow: hidden;
    box-shadow: 0 10px 24px rgba(0,0,0,.35);
  }

  /* ---------- shared brand lockup ---------- */
  .brand-lockup {
    position: absolute;
    display: flex;
    align-items: center;
    gap: 10px;
    font-family: "Montserrat", sans-serif;
    font-weight: 700;
    color: var(--leaf-green);
    white-space: nowrap;
  }
  .brand-lockup .brand-dot {
    display: inline-block;
    border-radius: 50%;
    background: var(--flame-orange);
    flex: none;
  }

  /* ---------- services side ---------- */
  .services-band {
    position: absolute;
    inset: 0;
    width: 100%;
    height: 100%;
  }
  .card--services .brand-lockup { left: 40px; top: 40px; font-size: 32px; }
  .card--services .brand-dot { width: 24px; height: 24px; }
  .services-ribbon {
    position: absolute;
    left: 120px;
    top: 118px;
    background: var(--earth-brown);
    color: var(--paper);
    font-family: "Roboto Condensed", sans-serif;
    font-weight: 700;
    font-size: 22px;
    letter-spacing: .5px;
    padding: 4px 38px;
  }
  .services-list {
    position: absolute;
    left: 20px;
    right: 20px;
    top: 196px;
    font-family: "Arimo", sans-serif;
    font-size: 12.5px;
    line-height: 1.55;
    color: var(--ink);
    text-align: center;
    white-space: nowrap;
  }

  /* ---------- contact side ---------- */
  .card--contact .brand-lockup { left: 34px; top: 34px; font-size: 28px; }
  .card--contact .brand-dot { width: 22px; height: 22px; }
  .contact-person { position: absolute; left: 40px; top: 96px; }
  .contact-person__name {
    font-weight: 700;
    font-size: 24px;
    color: var(--earth-brown);
    letter-spacing: .5px;
  }
  .contact-person__title {
    font-weight: 500;
    font-size: 13px;
    color: var(--ink);
    letter-spacing: .6px;
    margin-top: 2px;
  }
  .contact-list {
    position: absolute;
    left: 40px;
    top: 166px;
    list-style: none;
    font-size: 12.5px;
    line-height: 1.5;
    color: var(--ink);
  }
  .contact-list li { display: flex; align-items: center; gap: 10px; }
  .contact-list svg { width: 13px; height: 13px; flex: none; }
  .contact-list .no-icon { padding-left: 23px; }
  .brand-mark-area {
    position: absolute;
    right: 28px;
    top: 80px;
    width: 150px;
    height: 150px;
    border-radius: 50%;
    background: radial-gradient(circle at 40% 35%, #a8d36a 0%, var(--leaf-green) 55%, #5e9524 100%);
  }
</style>
</head>
<body>

  <!-- Back: list of services -->
  <section class="card card--services">
    <svg class="services-band" viewBox="0 0 540 309" preserveAspectRatio="none" aria-hidden="true">
      <polygon points="0,309 0,180 250,180 540,95 540,309" fill="var(--leaf-green)"/>
    </svg>
    <div class="brand-lockup"><span class="brand-dot"></span>Vardel GreenWorks</div>
    <div class="services-ribbon">OUR SERVICES</div>
    <p class="services-list">
      • LFG Engineering and Design • GCCS Planning and Operational Consulting<br>
      • Compliance Monitoring and Reporting • Routine Operations &amp; Maintenance<br>
      • Nonroutine O&amp;M • Construction Management • Construction QA<br>
      • GCCS Construction
    </p>
  </section>

  <!-- Front: contact details -->
  <section class="card card--contact">
    <div class="brand-lockup"><span class="brand-dot"></span>Vardel GreenWorks</div>
    <div class="brand-mark-area" role="img" aria-label="Large brand emblem area in green, brown and orange"></div>

    <div class="contact-person">
      <div class="contact-person__name">MARLON TESSARO</div>
      <div class="contact-person__title">MANAGING DIRECTOR</div>
    </div>

    <ul class="contact-list">
      <li>
        <svg viewBox="0 0 14 14" aria-hidden="true"><rect x="3.5" y="1" width="7" height="12" rx="1.5" fill="none" stroke="var(--leaf-green)" stroke-width="1.4"/><circle cx="7" cy="11" r=".8" fill="var(--leaf-green)"/></svg>
        044-310 582 617
      </li>
      <li>
        <svg viewBox="0 0 14 14" aria-hidden="true"><path d="M3 1.5l2.2 2.6-1.2 1.4c.8 1.8 2.2 3.2 4 4l1.4-1.2 2.6 2.2-1.4 2c-5 0-9.1-4.1-9.1-9.1z" fill="var(--leaf-green)"/></svg>
        044-310 582 618
      </li>
      <li>
        <svg viewBox="0 0 14 14" aria-hidden="true"><rect x="1" y="3" width="12" height="8.5" fill="var(--leaf-green)"/><path d="M1 3l6 5 6-5" fill="none" stroke="#fff" stroke-width="1.1"/></svg>
        info@vardelgreenworks.example
      </li>
      <li>
        <svg viewBox="0 0 14 14" aria-hidden="true"><circle cx="7" cy="7" r="5.8" fill="none" stroke="var(--leaf-green)" stroke-width="1.3"/><ellipse cx="7" cy="7" rx="2.4" ry="5.8" fill="none" stroke="var(--leaf-green)" stroke-width="1.1"/><path d="M1.2 7h11.6M2 4.3h10M2 9.7h10" stroke="var(--leaf-green)" stroke-width="1"/></svg>
        www.vardelgreenworks.example
      </li>
      <li class="no-icon">421, Address line goes here</li>
      <li class="no-icon">45452, Country name</li>
    </ul>
  </section>

</body>
</html>
```